Wedding Startup Full Website Design

We've just completed our online platform and need to create a website that represents our brand and vision, and clearly communicates our features and value proposition to potential users. There are a minimum of 4 pages that need to be designed. One geared toward wedding professionals (venues/vendors/coordinators), another toward engaged couples, one showcasing features, and an 'About Us' page.

The designer will creative freedom to create a unique UI/UX as long as it represents our brand and is relevant to our target audience/market. The ideal candidate will be able to assume the mindset of someone working in the wedding industry and/or an engaged couple. Ability to create illustrations is a plus.

Copy will be provided as needed. We will reimburse for stock images (pending approval before purchasing), but sourcing the stock images will be the responsibility of the designer.

Our current website: https://www.trelmora.com
Updates

Our project has now been guaranteed! We look forward to finding the perfect design for our site pages!

Still waiting for a design that stands out from the rest and aligns with the creative brief.

Target Market(s)

Wedding Professionals and Engaged Couples

Industry/Entity Type

Wedding

Number of Pages Required

4 page

Font styles to use
Sans Serif

Colors
ffffff
fbd4d5
f59195
33a6d7
cadf82
86cfc6

Requirements
Must have
• Common sense stuff like having a unified brand that accurately represents our platform, speaks to our target market, and clearly articulates our vision
Nice to have
• Illustrations
Should not have
• Overly cheesy or childish. We want to be professional but still embrace the wedding culture.

```html
<!DOCTYPE html>
<html lang="en">
<head>
<meta charset="utf-8">
<title>Trelmora — Smarter Wed Planning</title>
<link href="https://fonts.googleapis.com/css2?family=Raleway:wght@400;500;600;700&family=Open+Sans:wght@400;600&family=Great+Vibes&display=swap" rel="stylesheet">
<style>
:root{
  --white:#ffffff;
  --blush:#fbd4d5;
  --rose:#f59195;
  --rose-deep:#e8686d;
  --berry:#d9534f;
  --sky:#33a6d7;
  --button:#5aa9dd;
  --footer:#4f93cf;
  --ink:#333333;
  --muted:#666666;
  --soft-bg:#f7f7f7;
  --card-top:#ececec;
}
*{margin:0;padding:0;box-sizing:border-box}
html,body{width:1200px;height:3409px;overflow:hidden}
body{font-family:"Open Sans",Arial,sans-serif;color:var(--ink);background:var(--white);position:relative}
.abs{position:absolute}
.btn{position:absolute;background:var(--button);color:var(--white);font:600 12px "Raleway",sans-serif;letter-spacing:1px;text-transform:uppercase;display:flex;align-items:center;justify-content:center;box-shadow:0 2px 4px rgba(0,0,0,.15)}
.section-title{position:absolute;left:0;width:1200px;text-align:center;font:400 30px "Raleway",sans-serif;color:var(--ink)}
.divider{position:absolute;left:540px;width:120px;height:14px}

/* hero */
.hero{left:0;top:0;width:1200px;height:727px;background:linear-gradient(135deg,#6b5a55 0%,#a89a92 35%,#d9d2cc 55%,#8f8680 80%,#5e5651 100%)}
.nav{left:0;top:0;width:1200px;height:80px;background:rgba(0,0,0,.28)}
.logo{left:86px;top:18px;font:600 34px "Raleway",sans-serif;color:var(--rose);display:flex;align-items:center;gap:10px}
.logo .dot{width:12px;height:12px;border-radius:50%;background:var(--sky)}
.menu{left:454px;top:0;height:80px;display:flex;gap:0;font:600 11px "Raleway",sans-serif;color:var(--white);text-transform:uppercase}
.menu a{display:flex;align-items:center;padding:0 20px;height:80px;text-decoration:none;color:inherit;position:relative}
.menu a.active{color:var(--rose)}
.menu a.active::after{content:"";position:absolute;left:8px;right:8px;bottom:0;height:3px;background:var(--rose)}
.hero-badge{left:600px;top:443px}
.hero-badge .diamond{position:absolute;left:-205px;top:-205px;width:410px;height:410px}
.hero-text{position:absolute;left:-180px;top:-110px;width:360px;text-align:center;font-family:"Great Vibes",cursive}
.hero-text .welcome{font-size:44px;color:#3a3a3a}
.hero-text .name{font-size:84px;color:var(--rose);line-height:1.05}
.hero-text .tag{font-size:34px;color:#3a3a3a;line-height:1.15}
.dots{left:1066px;top:696px;display:flex;gap:8px}
.dots i{width:8px;height:8px;background:rgba(255,255,255,.5);display:block}
.dots i.on{background:var(--white)}

/* steps */
.step{position:absolute;width:280px;text-align:center}
.step .icon{width:96px;height:96px;border-radius:50%;background:var(--rose);margin:0 auto;display:flex;align-items:center;justify-content:center}
.step .icon.deep{background:var(--berry)}
.step h3{margin-top:25px;font:600 15px "Raleway",sans-serif;text-transform:uppercase;letter-spacing:.5px}
.step p{margin-top:12px;font-size:14px;line-height:22px;color:var(--muted)}
.step p a{color:var(--sky);text-decoration:none}

/* professionals */
.pros{left:0;top:1107px;width:1200px;height:636px;background:var(--soft-bg)}
.pro-grid{left:148px;top:1227px;width:904px;height:398px;display:grid;grid-template-columns:repeat(3,1fr);grid-template-rows:repeat(2,1fr);box-shadow:0 2px 8px rgba(0,0,0,.08)}
.pro-photo{position:relative}
.pro-text{background:var(--white);padding:32px 26px}
.pro-text h3{font:600 16px "Raleway",sans-serif;margin-bottom:12px}
.pro-text p{font-size:13px;line-height:22px;color:var(--muted)}

/* couples */
.couple-card{position:absolute;top:1864px;width:239px;height:295px;background:var(--rose);box-shadow:0 3px 8px rgba(0,0,0,.15);color:var(--white);text-align:center}
.couple-card svg.flap{position:absolute;left:0;top:0}
.couple-card h3{position:absolute;top:98px;left:0;width:100%;font:600 16px "Raleway",sans-serif}
.couple-card p{position:absolute;top:128px;left:22px;right:22px;font-size:13px;line-height:21px}

/* why */
.why-photo{left:0;top:2278px;width:614px;height:641px;background:linear-gradient(160deg,#e6d5d8 0%,#b9a6a9 40%,#8e8a94 70%,#d7c9c4 100%)}
.why-label{left:0;top:2798px;width:614px;height:52px;background:rgba(40,40,40,.7);color:var(--white);font:700 30px "Raleway",sans-serif;letter-spacing:.5px;padding-left:130px;display:flex;align-items:center;text-transform:uppercase}
.why-list{left:614px;top:2278px;width:586px;height:641px;background:var(--soft-bg);padding:72px 60px 0 61px}
.why-item{height:104px}
.why-item h3{font:600 16px "Raleway",sans-serif;margin-bottom:12px}
.why-item p{font-size:13px;line-height:22px;color:var(--muted)}

/* contact */
.contact{left:0;top:2919px;width:1200px;height:432px;background:linear-gradient(135deg,#2a2c33 0%,#4a4a52 45%,#6a6670 60%,#2c2d33 100%)}
.contact-logo{left:0;top:2972px;width:1200px;justify-content:center}
.contact-note{left:0;top:3056px;width:1200px;text-align:center;color:var(--white);font-size:14px}
.field{position:absolute;border:1px solid rgba(255,255,255,.55);color:rgba(255,255,255,.8);font-size:13px;padding:10px 12px}
.footer{left:0;top:3351px;width:1200px;height:58px;background:var(--footer);color:var(--white);font-size:12px}
.footer .copy{position:absolute;left:86px;top:20px}
.social{position:absolute;top:15px;width:28px;height:28px}
</style>
</head>
<body>

<!-- HERO -->
<div class="abs hero" role="img" aria-label="Photo of a groom placing a ring on the bride's hand above a white rose bouquet"></div>
<header class="abs nav">
  <div class="abs logo"><span class="dot"></span>Trelmora</div>
  <nav class="abs menu">
    <a class="active" href="#">Home</a>
    <a href="#">About Us</a>
    <a href="#">Wedding Professionals</a>
    <a href="#">Engaged Couples</a>
  </nav>
  <div class="btn" style="left:1000px;top:23px;width:114px;height:34px;font-size:11px">Access Demo</div>
</header>
<div class="abs hero-badge">
  <svg class="diamond" viewBox="0 0 410 410">
    <polygon points="205,8 402,205 205,402 8,205" fill="rgba(255,255,255,.82)" stroke="#ffffff" stroke-width="3"/>
    <polygon points="205,22 388,205 205,388 22,205" fill="none" stroke="#ffffff" stroke-width="1.5"/>
  </svg>
  <div class="hero-text">
    <div class="welcome">Welcome</div>
    <div class="name">Trelmora</div>
    <div class="tag">Smarter Wed<br>Planning</div>
  </div>
</div>
<div class="abs dots"><i></i><i></i><i class="on"></i></div>

<!-- HOW TO GET STARTED -->
<h2 class="section-title" style="top:772px">How To Get Started</h2>
<svg class="divider" style="top:812px" viewBox="0 0 120 14"><line x1="0" y1="7" x2="46" y2="7" stroke="#f59195"/><line x1="74" y1="7" x2="120" y2="7" stroke="#f59195"/><path d="M60 12 L54 6 A3 3 0 0 1 60 3 A3 3 0 0 1 66 6 Z" fill="#e8686d"/></svg>

<div class="step" style="left:108px;top:854px">
  <div class="icon"><svg width="44" height="44" viewBox="0 0 44 44" fill="none" stroke="#fff" stroke-width="3"><rect x="6" y="8" width="26" height="30" rx="2"/><line x1="12" y1="18" x2="24" y2="18"/><line x1="12" y1="25" x2="22" y2="25"/><path d="M38 8 L24 22 L22 28 L28 26 L42 12 Z" fill="#f59195"/></svg></div>
  <h3>Sign Up</h3>
  <p>Create a free account on Trelmora to<br>access popular collaboration tools.<br><a href="#">Get Started</a></p>
</div>
<svg class="abs" style="left:398px;top:900px" width="56" height="12" viewBox="0 0 56 12"><line x1="0" y1="6" x2="50" y2="6" stroke="#e8686d" stroke-width="2"/><path d="M46 1 L55 6 L46 11" fill="none" stroke="#e8686d" stroke-width="2"/></svg>
<div class="step" style="left:460px;top:854px">
  <div class="icon"><svg width="44" height="44" viewBox="0 0 44 44" fill="none" stroke="#fff" stroke-width="3"><rect x="6" y="8" width="26" height="30" rx="2"/><line x1="12" y1="18" x2="24" y2="18"/><line x1="12" y1="25" x2="22" y2="25"/><path d="M38 8 L24 22 L22 28 L28 26 L42 12 Z" fill="#f59195"/></svg></div>
  <h3>Collaborate</h3>
  <p>Add clients within the application to<br>better organize and manage event<br>details.</p>
</div>
<svg class="abs" style="left:748px;top:900px" width="56" height="12" viewBox="0 0 56 12"><line x1="0" y1="6" x2="50" y2="6" stroke="#e8686d" stroke-width="2"/><path d="M46 1 L55 6 L46 11" fill="none" stroke="#e8686d" stroke-width="2"/></svg>
<div class="step" style="left:812px;top:854px">
  <div class="icon deep"><svg width="44" height="44" viewBox="0 0 44 44" fill="none" stroke="#fff" stroke-width="3"><circle cx="22" cy="18" r="12"/><path d="M14 26 L22 38 L30 26"/><path d="M16 18 L21 22 L28 14"/></svg></div>
  <h3>Connect</h3>
  <p>Linking your bank account within Trelmora to<br>allow for seamless payments and<br>monitoring.</p>
</div>

<!-- WEDDING PROFESSIONALS -->
<section class="abs pros"></section>
<h2 class="section-title" style="top:1145px">Wedding Professionals</h2>
<svg class="divider" style="top:1185px" viewBox="0 0 120 14"><line x1="0" y1="7" x2="46" y2="7" stroke="#f59195"/><line x1="74" y1="7" x2="120" y2="7" stroke="#f59195"/><path d="M60 12 L54 6 A3 3 0 0 1 60 3 A3 3 0 0 1 66 6 Z" fill="#e8686d"/></svg>
<div class="abs pro-grid">
  <div class="pro-photo" role="img" aria-label="Photo of a decorated reception venue with draped ceiling" style="background:linear-gradient(180deg,#dfe9ef 0%,#c9b3c0 55%,#8e4a5e 100%)"></div>
  <div class="pro-text"><h3>Professional Venues</h3><p>It is a long established fact that a reader will be distracted by the readable content of a page when looking at its layout.</p></div>
  <div class="pro-photo" role="img" aria-label="Photo of a table set with glasses and red roses" style="background:linear-gradient(180deg,#2e2a2c 0%,#8d8489 45%,#e8e2e6 100%)"></div>
  <div class="pro-text"><h3>Professional Vendors</h3><p>It is a long established fact that a reader will be distracted by the readable content of a page when looking at its layout.</p></div>
  <div class="pro-photo" role="img" aria-label="Photo of a bride trying on a gown with a consultant" style="background:linear-gradient(135deg,#e9e4dc 0%,#b8aea4 50%,#7d7670 100%)"></div>
  <div class="pro-text"><h3>Coordinators</h3><p>It is a long established fact that a reader will be distracted by the readable content of a page when looking at its layout.</p></div>
</div>
<div class="btn" style="left:525px;top:1652px;width:150px;height:39px">Learn More</div>

<!-- ENGAGED COUPLES -->
<h2 class="section-title" style="top:1783px">Engaged Couples</h2>
<svg class="divider" style="top:1823px" viewBox="0 0 120 14"><line x1="0" y1="7" x2="46" y2="7" stroke="#f59195"/><line x1="74" y1="7" x2="120" y2="7" stroke="#f59195"/><path d="M60 12 L54 6 A3 3 0 0 1 60 3 A3 3 0 0 1 66 6 Z" fill="#e8686d"/></svg>

<div class="couple-card" style="left:86px">
  <svg class="flap" width="239" height="84" viewBox="0 0 239 84"><polygon points="0,0 239,0 239,12 120,80 0,12" fill="#ececec"/><path d="M100 38 Q120 22 140 38 Q120 54 100 38 Z" fill="none" stroke="#e8686d" stroke-width="2.5"/><circle cx="120" cy="38" r="5" fill="#e8686d"/></svg>
  <h3>Vision</h3>
  <p>Every couple has a vision of what their special day will be like. Trelmora provides the tools to clearly and concisely communicate that to others.</p>
</div>
<div class="couple-card" style="left:350px">
  <svg class="flap" width="239" height="84" viewBox="0 0 239 84"><polygon points="0,0 239,0 239,12 120,80 0,12" fill="#ececec"/><rect x="108" y="28" width="20" height="22" fill="none" stroke="#e8686d" stroke-width="2.5"/><path d="M134 24 L120 38 L118 44 L124 42 L138 28 Z" fill="#e8686d"/></svg>
  <h3>Create</h3>
  <p>Taking your vision and communicating it to others can be difficult. With Trelmora we provide tools to help make the process better, ensuring your wedding day isn't just a dream.</p>
</div>
<div class="couple-card" style="left:614px">
  <svg class="flap" width="239" height="84" viewBox="0 0 239 84"><polygon points="0,0 239,0 239,12 120,80 0,12" fill="#ececec"/><g fill="none" stroke="#e8686d" stroke-width="2.5"><rect x="104" y="26" width="32" height="24"/><line x1="104" y1="34" x2="136" y2="34"/><line x1="115" y1="26" x2="115" y2="50"/><line x1="125" y1="26" x2="125" y2="50"/></g></svg>
  <h3>Organize</h3>
  <p>We know every detail is important when it comes to your special day. That's why we make it easy to stay organized so nothing is left out or forgotten.</p>
</div>
<div class="couple-card" style="left:878px">
  <svg class="flap" width="239" height="84" viewBox="0 0 239 84"><polygon points="0,0 239,0 239,12 120,80 0,12" fill="#ececec"/><g fill="none" stroke="#e8686d" stroke-width="2.5"><rect x="114" y="22" width="12" height="9"/><line x1="120" y1="31" x2="120" y2="38"/><line x1="106" y1="38" x2="134" y2="38"/><line x1="106" y1="38" x2="106" y2="44"/><line x1="134" y1="38" x2="134" y2="44"/><line x1="120" y1="38" x2="120" y2="44"/><rect x="101" y="44" width="10" height="8"/><rect x="115" y="44" width="10" height="8"/><rect x="129" y="44" width="10" height="8"/></g></svg>
  <h3>Monitor</h3>
  <p>It's important to stay on track when planning. Within Trelmora you know exactly where you are in the process and what is needed to keep everything running smoothly.</p>
</div>
<div class="btn" style="left:525px;top:2189px;width:150px;height:39px">Learn More</div>

<!-- WHY CHOOSE -->
<div class="abs why-photo" role="img" aria-label="Photo of a bride and groom embracing under falling rose petals"></div>
<div class="abs why-label">Why Choose Trelmora</div>
<div class="abs why-list">
  <div class="why-item"><h3>Saves Everyone Time</h3><p>Trelmora streamlines certain processes allowing you to spend more time on the things your want to or just relax!</p></div>
  <div class="why-item"><h3>Simplified Organization</h3><p>Trelmora was built with organization in mind. All event details are in one place making executing an event easier.</p></div>
  <div class="why-item"><h3>Better Client Reviews</h3><p>With Trelmora you can offer your clients an experience they will rave about, leading to better reviews and more clients.</p></div>
  <div class="why-item"><h3>Lower Transaction Fees</h3><p>We offer the lowest online processing fees (2.65%) in the wedding industry, meaning you keep more of your money.</p></div>
  <div class="why-item"><h3>Accessible on Any Device</h3><p>Flexibility is key, which is why Trelmora's platform was built to be accessed on your phone, tablet or desktop.</p></div>
</div>

<!-- CONTACT -->
<section class="abs contact" role="img" aria-label="Dark photo of a couple holding hands"></section>
<div class="abs logo contact-logo" style="display:flex"><span class="dot"></span>Trelmora</div>
<p class="abs contact-note">Fill this form to contact us for any query.</p>
<div class="field" style="left:175px;top:3096px;width:411px;height:39px">Name</div>
<div class="field" style="left:614px;top:3096px;width:413px;height:39px">Email</div>
<div class="field" style="left:175px;top:3157px;width:852px;height:64px">Message</div>
<div class="btn" style="left:525px;top:3250px;width:150px;height:39px">Send</div>

<!-- FOOTER -->
<footer class="abs footer">
  <span class="copy">Copyright © 2018 &nbsp;|&nbsp; All rights reserved</span>
  <svg class="social" style="left:968px" viewBox="0 0 28 28"><polygon points="14,1 27,14 14,27 1,14" fill="none" stroke="#fff" stroke-width="1.2"/><circle cx="14" cy="14" r="3" fill="#fff"/></svg>
  <svg class="social" style="left:1027px" viewBox="0 0 28 28"><polygon points="14,1 27,14 14,27 1,14" fill="none" stroke="#fff" stroke-width="1.2"/><circle cx="14" cy="14" r="3" fill="#fff"/></svg>
  <svg class="social" style="left:1084px" viewBox="0 0 28 28"><polygon points="14,1 27,14 14,27 1,14" fill="none" stroke="#fff" stroke-width="1.2"/><circle cx="14" cy="14" r="3" fill="#fff"/></svg>
</footer>

</body>
</html>
```